Business Card Design

I have a very clear idea of what I want. I just do not know how to do the graphic design to match it.

On the front I want the uploaded image with the horse and the two people.
I want

Bottom left hand corner
Lewis Brand
0438 512 607

Bottom right
There is maroon block with Neil Patton Practitioner Group Logo
Next to that I want the Stable Arc tile about the same size ( attached psd file)

On the back I want a plain colour (white) with the information

Lewis Brand
Equine Performance
Rowland4Ponies and Acupuncture
Horsemanship Lessons and Clinics
Horse Training

lbrand@fauna812.com.au
FB/lewis.brand.207
StableArc.com.au

Industry/Entity Type

Business

Contact Information for Business Card

Lewis Brand
0438 512 607
lbrand@fauna812.com.au

```html
<!DOCTYPE html>
<html lang="en">
<head>
<meta charset="utf-8">
<title>Lewis Brand – Business Card</title>
<link rel="stylesheet" href="https://fonts.googleapis.com/css2?family=Cinzel:wght@400;600&family=Yellowtail&display=swap">
<style>
  :root {
    --backdrop: #2b2b2b;
    --maroon: #6a2413;
    --maroon-dark: #4a1a0d;
    --gold: #c9a12a;
    --ink: #2a1a12;
    --cream: #f1e6cf;
    --sand-light: #e2cfa5;
    --sand-mid: #c9ad7b;
    --sand-dark: #a98a58;
    --paper: #fbfaf7;
  }
  * { box-sizing: border-box; margin: 0; padding: 0; }
  html, body { width: 1200px; height: 1200px; overflow: hidden; }
  body { background: var(--backdrop); font-family: "Cinzel", serif; }
  .canvas { position: relative; width: 1200px; height: 1200px; }

  .card { position: absolute; left: 150px; width: 900px; height: 514px; overflow: hidden; }
  .card--front { top: 60px; }
  .card--back { top: 626px; background: var(--paper); }

  /* front */
  .card__photo {
    position: absolute; inset: 0;
    background: radial-gradient(ellipse at 50% 35%, var(--sand-light) 0%, var(--sand-mid) 60%, var(--sand-dark) 100%);
  }
  .headline { position: absolute; top: 20px; left: 0; width: 900px; height: 260px; color: var(--maroon-dark); }
  .headline__arcs { position: absolute; top: 0; left: 0; width: 900px; height: 260px; }
  .headline__lead {
    position: absolute; top: 36px; left: 0; width: 900px; text-align: center;
    font-size: 24px; line-height: 30px; letter-spacing: 1px; font-weight: 600; white-space: nowrap;
  }
  .headline__your {
    position: absolute; top: 86px; left: 470px;
    font-family: "Yellowtail", cursive; font-size: 40px; line-height: 40px;
  }
  .headline__main {
    position: absolute; top: 118px; left: 0; width: 900px; text-align: center;
    font-family: "Yellowtail", cursive; font-size: 100px; line-height: 104px; white-space: nowrap;
  }

  .identity { position: absolute; left: 0; top: 356px; width: 360px; }
  .identity__name {
    background: rgba(241, 230, 207, 0.55); color: var(--maroon-dark);
    font-size: 30px; padding: 4px 0 2px 60px; letter-spacing: 1px;
  }
  .identity__phone {
    display: flex; align-items: center; gap: 10px;
    background: var(--maroon); color: var(--gold);
    font-size: 26px; padding: 4px 0 4px 60px;
  }
  .identity__phone svg { width: 20px; height: 20px; }

  .partners { position: absolute; right: 18px; bottom: 18px; display: flex; align-items: flex-end; gap: 14px; }
  .partner-tile {
    width: 72px; height: 72px; background: var(--paper); border-radius: 10px;
    display: flex; align-items: center; justify-content: center; text-align: center;
    color: var(--maroon); font-size: 11px; font-weight: 600; line-height: 1.2;
  }
  .partner-block {
    width: 110px; height: 110px; background: var(--maroon);
    display: flex; align-items: center; justify-content: center; text-align: center;
    color: var(--gold); font-size: 12px; line-height: 1.3; padding: 8px;
  }

  /* back */
  .tab { position: absolute; width: 340px; height: 34px; }
  .tab--top { top: 0; left: 330px; }
  .tab--bottom { bottom: 0; left: 200px; }
  .back__name { position: absolute; left: 110px; top: 120px; color: var(--gold); font-size: 32px; font-weight: 400; letter-spacing: 1px; }
  .services { position: absolute; left: 110px; top: 178px; list-style: none; }
  .services li { color: var(--ink); font-size: 16px; line-height: 1.55; display: flex; align-items: center; gap: 12px; }
  .services li::before { content: ""; width: 6px; height: 6px; border-radius: 50%; background: var(--gold); }
  .divider { position: absolute; left: 470px; top: 150px; width: 3px; height: 270px; background: var(--maroon); }
  .contacts { position: absolute; left: 510px; top: 228px; list-style: none; }
  .contacts li { font-size: 17px; line-height: 1.5; color: var(--ink); }
  .contacts .contacts__accent { color: var(--gold); }
</style>
</head>
<body>
<main class="canvas">

  <section class="card card--front">
    <div class="card__photo" role="img" aria-label="Sandy arena photograph: a man in a hat and jeans watching as a woman lunges a bay horse"></div>

    <div class="headline">
      <svg class="headline__arcs" viewBox="0 0 900 260" aria-hidden="true">
        <path d="M290 30 Q450 8 610 30" fill="none" stroke="#4a1a0d" stroke-width="2"/>
        <path d="M290 86 Q450 68 610 86" fill="none" stroke="#4a1a0d" stroke-width="2"/>
        <path d="M250 238 Q450 254 650 230" fill="none" stroke="#4a1a0d" stroke-width="3"/>
      </svg>
      <p class="headline__lead">HOW YOU EVER GONNA KNOW</p>
      <p class="headline__your">Your</p>
      <p class="headline__main">Potential</p>
    </div>

    <div class="identity">
      <p class="identity__name">LEWIS BRAND</p>
      <p class="identity__phone">
        <svg viewBox="0 0 24 24" aria-hidden="true"><path fill="#c9a12a" d="M6.6 10.8a15 15 0 0 0 6.6 6.6l2.2-2.2c.3-.3.7-.4 1-.2 1.1.4 2.3.6 3.6.6.6 0 1 .4 1 1V20c0 .6-.4 1-1 1A17 17 0 0 1 3 4c0-.6.4-1 1-1h3.5c.6 0 1 .4 1 1 0 1.3.2 2.5.6 3.6.1.3 0 .7-.2 1z"/></svg>
        0438 512 607
      </p>
    </div>

    <div class="partners">
      <div class="partner-tile">Stable<br>Arc</div>
      <div class="partner-block">Neil Patton Practitioner Group</div>
    </div>
  </section>

  <section class="card card--back">
    <svg class="tab tab--top" viewBox="0 0 340 34" aria-hidden="true"><polygon points="0,0 340,0 310,34 30,34" fill="#6a2413"/></svg>
    <svg class="tab tab--bottom" viewBox="0 0 340 34" aria-hidden="true"><polygon points="30,0 310,0 340,34 0,34" fill="#6a2413"/></svg>

    <h1 class="back__name">LEWIS BRAND</h1>
    <ul class="services">
      <li>EQUINE PERFORMANCE</li>
      <li>ROWLAND4PONIES AND ACUPUNCTURE</li>
      <li>HORSEMANSHIP LESSONS AND CLINICS</li>
      <li>HORSE TRAINING</li>
    </ul>

    <div class="divider"></div>

    <ul class="contacts">
      <li>LBRAND@FAUNA812.COM.AU</li>
      <li>FB/LEWIS.BRAND.207</li>
      <li>STABLEARC.COM.AU</li>
      <li class="contacts__accent">0438 512 607</li>
      <li class="contacts__accent">LBRAND@FAUNA812.COM.AU</li>
    </ul>
  </section>

</main>
</body>
</html>
```